Website Design - Financial Services Software

We are looking for website designs for our public website.
Some competitor sites we like are
www.torvani.com.au
www.pluma.com.au
www.quentabridge.com
www.morlupa.com.au

A wireframe example of our site can be found at
http://pr4tqz.bivlowpage.com/

Attached is our logo.

Industry/Entity Type

Financial

```html
<!DOCTYPE html>
<html lang="en">
<head>
<meta charset="utf-8">
<title>Varentis – Smarter Financial Strategies</title>
<link rel="stylesheet" href="https://fonts.googleapis.com/css2?family=Lato:ital,wght@0,400;0,700;0,900;1,700&display=swap">
<style>
:root{
  --navy:#0b2340;
  --gold:#8a5b14;
  --gold-text:#7d5010;
  --yellow:#f6c623;
  --ink:#111;
  --body:#333;
  --footer:#2e2e2e;
  --footer-dark:#1f1f1f;
  --white:#fff;
}
*{box-sizing:border-box;margin:0;padding:0}
html,body{width:1200px;height:1175px;overflow:hidden}
body{position:relative;font-family:'Lato',sans-serif;color:var(--body);background:var(--white)}
.abs{position:absolute}

.topbar{left:0;top:0;width:1200px;height:32px;background:var(--navy)}
.login{left:980px;top:4px;width:79px;height:24px;background:var(--yellow);color:var(--ink);font-size:16px;display:flex;align-items:center;justify-content:center;gap:6px}
.header{left:0;top:32px;width:1200px;height:85px;background:linear-gradient(#fdfdfd,#eeeeee);border-bottom:1px solid #ccc}
.brand-mark{left:132px;top:14px;width:80px;height:96px;background:var(--white);display:flex;align-items:center;justify-content:center}
.brand-mark span{display:block;width:56px;height:64px;background:var(--gold)}
.brand-name{left:216px;top:58px;color:var(--gold);font-size:29px;font-weight:700;letter-spacing:1px;line-height:1}
.brand-tag{left:216px;top:88px;color:var(--gold);font-size:10.5px;font-weight:700;line-height:1}
.nav a{position:absolute;top:58px;height:35px;line-height:35px;font-size:15px;color:#333;text-decoration:none;text-transform:uppercase}
.nav .active{left:645px;width:97px;background:var(--gold);color:var(--white);text-align:center;border-radius:2px}

.hero{left:0;top:117px;width:1200px;height:418px;border-bottom:1px solid #ccc;
  background:linear-gradient(115deg,#e4dcd6 0%,#c9d6e8 18%,#9fb5d3 34%,#d6e0ee 52%,#e9e3de 70%,#f2efed 85%,#e6e6ea 100%)}
.hero-veil{left:0;top:117px;width:1200px;height:418px;background:linear-gradient(90deg,rgba(255,255,255,.55),rgba(255,255,255,.25) 45%,rgba(255,255,255,.5))}
.hero-title{left:131px;top:185px;font-size:30px;font-weight:700;color:var(--ink)}
.hero-sub{left:131px;top:239px;font-size:24px;line-height:29px;color:var(--ink);width:430px}
.tour-label{left:132px;top:322px;font-size:15px;font-weight:700;color:#333}
.tour-card{top:355px;width:194px;height:133px;border:2px solid #e2c35a;background:#fff}
.tour-card h3{height:30px;line-height:30px;text-align:center;font-size:17px;font-weight:700;color:var(--ink);background:linear-gradient(#f2c94f,#d79f1e)}
.tour-card .photo{height:99px}
.photo.practice{background:linear-gradient(100deg,#e8e6e2 0%,#b7b9bf 22%,#2c2e36 45%,#d9c2ad 55%,#2a2a30 70%,#cfd0d4 100%)}
.photo.dealer{background:linear-gradient(100deg,#1f2430 0%,#5c6270 25%,#c8cdd6 45%,#7c6454 62%,#e4dfda 80%,#3a3a40 100%)}
.slide-arrow{top:312px;width:28px;height:28px}
.video{left:552px;top:164px;width:517px;height:324px;background:#8a8a8a;padding:9px}
.video .screen{position:relative;width:499px;height:306px;
  background:linear-gradient(100deg,#5f7e9e 0%,#7fa3cf 20%,#4f7fbf 38%,#e6e9ee 55%,#2b2c32 72%,#4a4c52 85%,#d8dde2 100%)}
.v-badge{position:absolute;left:10px;top:10px;width:59px;height:59px;background:#333;border:2px solid #555}
.v-title{position:absolute;left:72px;top:10px;background:#222;color:#1fb6ea;font-size:16px;padding:0 4px;height:22px;line-height:22px}
.v-from{position:absolute;left:72px;top:35px;background:#222;color:#fff;font-size:11px;padding:0 4px;height:16px;line-height:16px}
.v-from b{color:#1fb6ea;font-weight:400}
.v-btn{position:absolute;left:450px;width:41px;height:31px;background:#222;border-radius:3px;color:#fff;font-size:7px;text-align:center}
.v-btn svg{display:block;margin:3px auto 1px}
.v-bar{position:absolute;left:10px;top:271px;width:480px;height:30px}

.section-icon{left:132px;top:563px;width:27px;height:34px;background:var(--gold)}
.section-title{left:172px;top:565px;font-size:25px;font-weight:400;color:var(--gold)}
.section-title small{font-size:20px;color:var(--navy)}
.section-rule{left:172px;top:599px;width:897px;height:1px;background:#bbb}
.intro{left:132px;top:609px;width:388px;font-size:13.2px;line-height:18.6px;color:#222}
.intro p+p{margin-top:10px}
.intro .hl{color:var(--gold-text);font-weight:700}
.intro .hl i{font-style:italic}
.read-more{left:131px;top:817px;width:94px;height:24px;background:var(--gold-text);color:#fff;font-size:13px;font-weight:700;line-height:24px;text-align:center}
.thumb{width:159px;height:99px;border:3px solid #ddd}
.t1{background:linear-gradient(135deg,#f2f2f4 0%,#e3d7d0 35%,#c9d2e4 60%,#4f7fc0 80%,#efe9e6 100%)}
.t2{border-color:var(--gold);background:linear-gradient(135deg,#bfc6cf 0%,#eef1f4 40%,#5b8fc4 65%,#2f5e96 100%);display:flex;align-items:flex-end}
.t2 span{width:100%;height:24px;line-height:24px;text-align:center;color:#fff;font-weight:700;font-size:14px;background:rgba(138,91,20,.9)}
.t3{background:linear-gradient(135deg,#2a2a2e 0%,#eeeeee 25%,#e8453a 40%,#f4c430 55%,#3aa0d8 72%,#f2f2f2 100%)}
.t4{background:linear-gradient(135deg,#5a6070 0%,#c4c8d0 30%,#eef0f4 55%,#d04a4a 75%,#f4f4f6 100%)}
.t5{background:linear-gradient(100deg,#f0ece6 0%,#c99a72 25%,#20242a 50%,#7cbc3a 72%,#e9f0dd 100%)}
.t6{background:linear-gradient(135deg,#d23a7c 0%,#5b7fd1 25%,#e8ecf6 50%,#c9d3ea 70%,#1e1e22 100%)}

.cta{left:131px;top:879px;width:938px;height:65px;background:var(--navy);border-radius:2px}
.cta-text{left:247px;top:898px;font-size:21px;color:#fff}
.cta-text b{font-weight:700}
.cta-btn{left:800px;top:893px;width:160px;height:38px;background:linear-gradient(#ffd95a,#e9a915);border-radius:4px;color:var(--gold-text);font-size:19px;font-weight:900;text-align:center;line-height:38px}

.footer{left:0;top:982px;width:1200px;height:154px;background:var(--footer)}
.foot-mark{left:170px;top:1002px;width:68px;height:80px;background:#fff}
.foot-name{left:132px;top:1084px;font-size:30px;font-weight:400;color:#fff;letter-spacing:1px;line-height:1}
.foot-col h4{font-size:20px;font-weight:400;color:#fff;padding-bottom:4px;border-bottom:1px solid #555;margin-bottom:6px}
.foot-col a{display:block;color:#eee;font-size:13.5px;line-height:21px;text-decoration:none}
.social{display:flex;align-items:center;gap:13px;color:#fff;font-size:13.5px}
.social i{display:block;width:22px;height:22px;border-radius:50%;background:#fff}
.copyright{left:0;top:1136px;width:1200px;height:39px;background:var(--footer-dark);color:#ddd;font-size:13.5px;text-align:center;line-height:39px}
</style>
</head>
<body>

<div class="abs topbar"></div>
<div class="abs login">
  <svg width="16" height="14" viewBox="0 0 16 14"><circle cx="8" cy="4" r="3.5" fill="#111"/><path d="M1 14c0-4 3-6 7-6s7 2 7 6z" fill="#111"/></svg>
  Login
</div>

<header class="abs header"></header>
<div class="abs brand-mark"><span></span></div>
<div class="abs brand-name">VARENTIS</div>
<div class="abs brand-tag">SMARTER FINANCIAL STRATEGIES</div>
<nav class="nav">
  <a class="active" href="#">Features</a>
  <a href="#" style="left:784px">Examples</a>
  <a href="#" style="left:911px">FAQ</a>
  <a href="#" style="left:997px">About</a>
</nav>

<section class="abs hero" role="img" aria-label="Soft photo of hands holding a tablet showing financial bar charts"></section>
<div class="abs hero-veil"></div>
<svg class="abs slide-arrow" style="left:76px" viewBox="0 0 28 28"><circle cx="14" cy="14" r="12.5" fill="none" stroke="#999" stroke-width="2.5"/><circle cx="14" cy="14" r="8" fill="#aaa"/><path d="M16 10l-4 4 4 4" stroke="#fff" stroke-width="2" fill="none"/></svg>
<svg class="abs slide-arrow" style="left:1096px" viewBox="0 0 28 28"><circle cx="14" cy="14" r="12.5" fill="none" stroke="#999" stroke-width="2.5"/><circle cx="14" cy="14" r="8" fill="#aaa"/><path d="M12 10l4 4-4 4" stroke="#fff" stroke-width="2" fill="none"/></svg>

<h1 class="abs hero-title">Smarter Financial Strategies</h1>
<p class="abs hero-sub">Value And Cash-flow Focused Financial Software For Financial Planners</p>
<p class="abs tour-label">Feature Tour:</p>
<div class="abs tour-card" style="left:131px">
  <h3>For Planning Practices</h3>
  <div class="photo practice" role="img" aria-label="Photo of a planning team in suits at a meeting table"></div>
</div>
<div class="abs tour-card" style="left:336px">
  <h3>For Dealer Groups</h3>
  <div class="photo dealer" role="img" aria-label="Photo of business people reviewing a laptop together"></div>
</div>

<div class="abs video">
  <div class="screen" role="img" aria-label="Video still of two advisers in an office reviewing documents at a desk">
    <div class="v-badge"></div>
    <div class="v-title">Smarter Financial Strategies</div>
    <div class="v-from">from <b>Varentis</b></div>
    <div class="v-btn" style="top:10px"><svg width="16" height="14" viewBox="0 0 16 14"><path d="M8 13L2 7a3.3 3.3 0 0 1 6-4 3.3 3.3 0 0 1 6 4z" fill="#fff"/></svg>LIKE</div>
    <div class="v-btn" style="top:47px"><svg width="16" height="14" viewBox="0 0 16 14"><circle cx="8" cy="7" r="6.5" fill="#fff"/></svg>LATER</div>
    <div class="v-btn" style="top:84px"><svg width="16" height="14" viewBox="0 0 16 14"><circle cx="3" cy="11" r="1.5" fill="#fff"/><circle cx="8" cy="7" r="1.5" fill="#fff"/><circle cx="13" cy="3" r="1.5" fill="#fff"/><circle cx="13" cy="11" r="1.5" fill="#fff"/><path d="M3 11L13 3M8 7l5 4" stroke="#fff"/></svg>SHARE</div>
    <div class="v-btn" style="top:121px"><svg width="16" height="14" viewBox="0 0 16 14"><path d="M5 3L1 7l4 4M11 3l4 4-4 4M9 2L7 12" stroke="#fff" stroke-width="1.8" fill="none"/></svg>EMBED</div>
    <svg class="v-bar" viewBox="0 0 480 30">
      <rect x="0" y="0" width="58" height="30" rx="3" fill="#222"/>
      <path d="M23 8l14 7-14 7z" fill="#fff"/>
      <rect x="66" y="0" width="414" height="30" rx="3" fill="#222"/>
      <rect x="75" y="10" width="310" height="9" fill="#fff"/>
      <rect x="75" y="10" width="240" height="9" fill="#888"/>
      <rect x="75" y="10" width="85" height="9" fill="#1fb6ea"/>
      <g fill="#1fb6ea"><rect x="395" y="9" width="2" height="11"/><rect x="399" y="9" width="2" height="11"/><rect x="403" y="9" width="2" height="11"/><rect x="407" y="9" width="2" height="11"/><rect x="411" y="9" width="2" height="11"/><rect x="415" y="9" width="2" height="11"/><rect x="419" y="9" width="2" height="11"/><rect x="423" y="9" width="2" height="11"/></g>
      <text x="434" y="20" fill="#1fb6ea" font-family="Lato,sans-serif" font-size="13">HD</text>
      <path d="M462 10l4 4M470 10l-4 4M462 20l4-4M470 20l-4-4" stroke="#fff" stroke-width="2"/>
    </svg>
  </div>
</div>

<div class="abs section-icon"></div>
<h2 class="abs section-title">Varentis <small>Smarter Financial Strategies</small></h2>
<div class="abs section-rule"></div>
<div class="abs intro">
  <p>Lorem ipsum dolor sit amet, consectetur adipiscing elit. Proin odio lacus, tempus et sollicitudin at, gravida eu ligula. Etiam phar massa odio, eget fringilla odio vehicula non. Sed vel lacus bibendum nunc consequat elementum. In nibh massa, rutrum sed pulvii consequat et nisl. <span class="hl">Nam pretium ut dolor eu fringilla. in Morbi viverra</span> dolreu sollicitudin. Praesent volutpat porta metus.</p>
  <p>Phasellus convallis eget nisl nec imperdiet. Pellentesque arcu erat convallis eu diam imperdiet, <span class="hl"><i>varius malesuada leo. Suspendisse ac turpis facilisis, convallis</i></span> purus quis, dictum est. Nullam at arcu or massa tincidunt elementum.</p>
</div>
<div class="abs read-more">Read More »</div>

<div class="abs thumb t1" style="left:557px;top:625px" role="img" aria-label="Photo of hands with pens over a printed pie chart"></div>
<div class="abs thumb t2" style="left:736px;top:625px" role="img" aria-label="Photo of a laptop and tablet showing a blue report"><span>FEATURE 2</span></div>
<div class="abs thumb t3" style="left:910px;top:625px" role="img" aria-label="Photo of colourful pie and bar charts beside a keyboard and calculator"></div>
<div class="abs thumb t4" style="left:557px;top:743px" role="img" aria-label="Photo of a calculator on financial papers"></div>
<div class="abs thumb t5" style="left:736px;top:743px" role="img" aria-label="Photo of three smiling colleagues in office wear"></div>
<div class="abs thumb t6" style="left:910px;top:743px" role="img" aria-label="Photo of a hand pointing at a chart on a monitor"></div>

<div class="abs cta"></div>
<p class="abs cta-text">Create an account today and begin your <b>30 days Trial!</b></p>
<div class="abs cta-btn">SIGN UP NOW !</div>

<footer class="abs footer"></footer>
<div class="abs foot-mark"></div>
<div class="abs foot-name">VARENTIS</div>
<div class="abs foot-col" style="left:354px;top:998px;width:97px"><h4>About</h4><a href="#">About Us</a><a href="#">Support</a></div>
<div class="abs foot-col" style="left:514px;top:998px;width:164px"><h4>Getting Started</h4><a href="#">Why Varentis</a><a href="#">Download &amp; Summary</a><a href="#">Varentis Videos</a></div>
<div class="abs foot-col" style="left:741px;top:998px;width:96px"><h4>Legal</h4><a href="#">Tearms of Use</a><a href="#">Privacy</a></div>
<div class="abs foot-col" style="left:904px;top:998px;width:160px"><h4>Connect</h4></div>
<div class="abs social" style="left:898px;top:1045px"><i></i>Varentis on Linkwell</div>
<div class="abs social" style="left:898px;top:1079px"><i></i>Varentis on Chirper</div>
<div class="abs copyright">Copyright © 2014 Varentis Pty Ltd. All Right Reserved</div>

</body>
</html>
```